Business Card

I want our business cards to have a little more pizzazz. I like the content, and we are in healthcare (so nothing to wild or artsy), but something that allows our cards to stand out.

Business

```html
<!DOCTYPE html>
<html lang="en">
<head>
<meta charset="UTF-8">
<title>Velmed Supply – Business Card</title>
<link rel="stylesheet" href="https://fonts.googleapis.com/css2?family=Source+Sans+3:ital,wght@0,400;0,600;1,400&display=swap">
<style>
  :root {
    --brand-blue: #174a7e;
    --paper: #e9eaec;
    --backdrop: #8a8c8b;
    --text-dark: #3b3b3b;
    --text-grey: #8a8a8a;
    --white: #ffffff;
  }
  * { margin: 0; padding: 0; box-sizing: border-box; }
  html, body { width: 1200px; height: 900px; overflow: hidden; }
  body {
    background: var(--backdrop);
    font-family: "Source Sans 3", Arial, sans-serif;
    position: relative;
  }
  .card {
    position: absolute;
    left: 321px;
    width: 507px;
    height: 289px;
  }
  .card--front { top: 119px; background: var(--brand-blue); color: var(--white); }
  .card--back { top: 470px; background: var(--paper); color: var(--text-dark); }

  .front-wordmark {
    position: absolute;
    left: 52px; top: 112px;
    font-size: 27px; font-weight: 400; line-height: 1;
    color: var(--white);
  }
  .front-divider {
    position: absolute;
    left: 265px; top: 92px;
    width: 1px; height: 90px;
    background: rgba(255,255,255,0.6);
  }
  .services {
    position: absolute;
    left: 293px; top: 91px;
    list-style: none;
    font-style: italic;
    font-size: 14px;
    line-height: 22.5px;
  }
  .hotline {
    position: absolute;
    left: 0; right: 0; top: 226px;
    text-align: center;
    font-weight: 600;
    font-size: 15.5px;
    line-height: 20px;
  }

  .back-wordmark {
    position: absolute;
    left: 26px; top: 28px;
    font-size: 36px; font-weight: 400; line-height: 1;
    color: var(--brand-blue);
  }
  .contact {
    position: absolute;
    left: 33px; top: 100px;
  }
  .contact__name { font-size: 19px; font-weight: 600; color: var(--brand-blue); line-height: 24px; }
  .contact__title { font-size: 14px; color: var(--text-grey); line-height: 18px; margin-bottom: 6px; }
  .contact__line { font-size: 12.5px; line-height: 16px; }
  .contact__main { font-size: 12.5px; font-weight: 600; line-height: 18px; margin-bottom: 4px; }
  .contact__main span { color: var(--brand-blue); }
  .contact__row {
    display: flex; align-items: center; gap: 6px;
    font-size: 12.5px; line-height: 19.5px;
  }
  .contact__row svg { width: 13px; height: 13px; fill: var(--brand-blue); }

  .back-mark {
    position: absolute;
    left: 246px; top: 24px;
    width: 242px; height: 242px;
    border-radius: 50%;
    background: var(--brand-blue);
  }
</style>
</head>
<body>
  <section class="card card--front">
    <div class="front-wordmark">Velmed Supply</div>
    <div class="front-divider"></div>
    <ul class="services">
      <li>Servicing Laboratories</li>
      <li>Hospital &amp; Medical centers</li>
      <li>Reserch Facilities</li>
      <li>surgical Centers</li>
    </ul>
    <p class="hotline">you can’t reach me, please call our<br>Customer Service Hotline at 555.210.4411</p>
  </section>

  <section class="card card--back">
    <div class="back-wordmark">Velmed Supply</div>
    <div class="contact">
      <p class="contact__name">Daniel Morrow</p>
      <p class="contact__title">Territory manager</p>
      <p class="contact__line">48 Harbor Street</p>
      <p class="contact__line">Fairview, NJ 07022</p>
      <p class="contact__main"><span>P</span> : 555.210.4400</p>
      <p class="contact__row">
        <svg viewBox="0 0 16 16" aria-hidden="true"><path d="M3.5 1l2.5 3-1.5 2c1 2 3 4 5 5l2-1.5 3 2.5-1.5 2.5C8 15 1 8 1 2.5z"/></svg>
        (555) 318-2204
      </p>
      <p class="contact__row">
        <svg viewBox="0 0 16 16" aria-hidden="true"><path d="M4 1h8v4H4zM1 6h14v6h-3v3H4v-3H1zm4 4v4h6v-4z"/></svg>
        (555) 318-2290
      </p>
      <p class="contact__row">
        <svg viewBox="0 0 16 16" aria-hidden="true"><path d="M1 3h14v10H1zm1.5 1.2v.6L8 9l5.5-4.2v-.6z"/></svg>
        daniel.morrow@velmedsupply.com
      </p>
    </div>
    <div class="back-mark"></div>
  </section>
</body>
</html>
```